Postcard Mail Out - Wendell

We are a real estate company. We need a post card to mail out to potential clients to try and sale their land. We will attached a couple of post cards that we like but we do not want to copy them completely. We do need to put the Fair Dwelling Access and the Homevest logos with a disclosure saying not intended to solicit currently listed properties. The image below is what we had started working on. We would like to include something about farm land, timber, maybe a pond, something along those lines. The PDF Files attached are a flyer that was mailed out by another company that we do not want to copy completely. Attached also will be our company's Logo.

Requirements
Must have
• We do need to put the Fair Dwelling Access and the Homevest logos with a disclosure saying not intended to solicit currently listed properties.<br/><br/>At Sol Brantham Summit Realty, we are blessed to have one of the very best Rural Land Specialists available. Wendell has years of experience promoting and selling rural land properties. Wendell has earned the trust of many landowners, as he is so PASSIONATE in all regards to rural land, farms and ranches. He has made a wide range of landowners very happy throughout his years in Real Estate. Call him today and show him your property, and he will provide you with a free analysis and strategy to maximize the return on your property.
Nice to have
• A picture of Wendell has been added to use on the back of the post card with his phone and number. It would be nice to have a east Texas scenery picture behind him instead of an office.<br/><br/>Please include front and back of post card in your submission.
Should not have
• Should not have Marcus Vell's information on the postcard. That post card was just to show what we was wanting. The agent we want listed is Wendell Harbin and his phone number is (555)214-3098.

```html
<!DOCTYPE html>
<html lang="en">
<head>
<meta charset="utf-8">
<title>Rural Land Postcard – Front and Back</title>
<link href="https://fonts.googleapis.com/css2?family=Montserrat:wght@400;600;700;800&family=Libre+Baskerville:wght@700&display=swap" rel="stylesheet">
<style>
  :root {
    --page-bg: #e9eaec;
    --ink: #1f1f1f;
    --panel-dark: #232323;
    --accent-yellow: #e2e61c;
    --paper: #ffffff;
    --muted-text: #b8b8b8;
    --sky-top: #aeb9c9;
    --sky-low: #dfe3e6;
    --field-green: #5e8a2a;
    --field-light: #a9c36a;
    --forest-trunk: #8a5a32;
    --forest-green: #4f7a2c;
    --pond-blue: #5f86a8;
    --pond-green: #6f9440;
    --faded-tree: #b9c59a;
  }
  * { margin: 0; padding: 0; box-sizing: border-box; }
  html, body { width: 1200px; height: 800px; overflow: hidden; }
  body {
    background: var(--page-bg);
    font-family: "Montserrat", sans-serif;
    display: flex;
    align-items: center;
    justify-content: center;
    gap: 40px;
  }
  .postcard {
    width: 560px;
    height: 373px;
    position: relative;
    overflow: hidden;
    box-shadow: 0 6px 18px rgba(0,0,0,0.18);
    background: var(--paper);
  }

  /* Back side */
  .back-info {
    position: absolute;
    left: 0; top: 0;
    width: 290px; height: 287px;
    background: var(--panel-dark);
    color: var(--paper);
    padding: 24px 22px 0 22px;
  }
  .back-heading {
    color: var(--accent-yellow);
    font-weight: 700;
    font-size: 17px;
    margin-bottom: 6px;
  }
  .back-body {
    font-size: 11.5px;
    line-height: 1.32;
    font-weight: 400;
  }
  .back-address {
    margin-top: 12px;
    color: var(--muted-text);
    font-size: 10.5px;
    line-height: 1.3;
  }
  .contact-band {
    position: absolute;
    left: 0; bottom: 0;
    width: 290px; height: 86px;
    background: var(--accent-yellow);
    color: var(--ink);
    padding: 14px 18px;
    font-weight: 700;
    font-size: 21px;
    line-height: 1.35;
  }
  .contact-line { display: flex; align-items: center; gap: 10px; white-space: nowrap; }
  .contact-line svg { width: 20px; height: 20px; flex: none; }
  .contact-line.web { font-size: 17px; }
  .stamp-box {
    position: absolute;
    right: 28px; top: 22px;
    width: 72px; height: 82px;
    border: 1.5px solid var(--ink);
  }

  /* Front side */
  .front-art { display: block; width: 100%; height: 100%; }
  .headline { font-family: "Libre Baskerville", serif; font-weight: 700; }
  .subhead { font-family: "Montserrat", sans-serif; font-weight: 700; }
  .brand-name { font-family: "Libre Baskerville", serif; font-weight: 700; }
  .disclosure { font-family: "Libre Baskerville", serif; }
  .badge-caption { font-family: "Montserrat", sans-serif; font-weight: 600; }
</style>
</head>
<body>

<!-- Back of postcard -->
<section class="postcard postcard-back" aria-label="Postcard back">
  <div class="back-info">
    <h2 class="back-heading">Meet Wendell Harbin</h2>
    <p class="back-body">At Sol Brantham Summit Realty, we are blessed to have one of the very best Rural Land Specialists available. Wendell has years of experience promoting and selling rural land, farms and ranches, and has earned the trust of many landowners. Call him today and show him your property for a free analysis and strategy to maximize your return.</p>
    <p class="back-address">Business Address<br>No. 3 Design Road<br>1234 Reeper Works<br>TL, Country</p>
  </div>
  <div class="contact-band">
    <div class="contact-line phone">
      <svg viewBox="0 0 24 24" aria-hidden="true"><path d="M7 3c-1.5 1-3 2.5-3 5 0 6 6 13 12 13 2.5 0 4-1.5 5-3l-4-3-2 2c-3-1-6-4-7-7l2-2z" fill="none" stroke="#1f1f1f" stroke-width="2.2" stroke-linejoin="round"/></svg>
      <span>(555)214-3098</span>
    </div>
    <div class="contact-line web">
      <svg viewBox="0 0 24 24" aria-hidden="true"><g fill="none" stroke="#1f1f1f" stroke-width="2"><circle cx="12" cy="12" r="9.5"/><ellipse cx="12" cy="12" rx="4" ry="9.5"/><path d="M2.5 12h19M4.5 7h15M4.5 17h15"/></g></svg>
      <span>summitlandprop.com</span>
    </div>
  </div>
  <div class="stamp-box" aria-label="Stamp area"></div>
</section>

<!-- Front of postcard -->
<section class="postcard postcard-front" aria-label="Postcard front">
  <svg class="front-art" viewBox="0 0 600 400" xmlns="http://www.w3.org/2000/svg">
    <defs>
      <linearGradient id="skyFill" x1="0" y1="0" x2="0" y2="1">
        <stop offset="0" stop-color="var(--sky-top)"/>
        <stop offset="1" stop-color="var(--sky-low)"/>
      </linearGradient>
      <linearGradient id="forestFill" x1="0" y1="0" x2="0" y2="1">
        <stop offset="0" stop-color="var(--forest-trunk)"/>
        <stop offset="0.6" stop-color="#7a6a3a"/>
        <stop offset="1" stop-color="var(--forest-green)"/>
      </linearGradient>
      <linearGradient id="fieldFill" x1="0" y1="0" x2="0" y2="1">
        <stop offset="0" stop-color="#c9d6df"/>
        <stop offset="0.3" stop-color="var(--field-light)"/>
        <stop offset="1" stop-color="var(--field-green)"/>
      </linearGradient>
      <linearGradient id="pondFill" x1="0" y1="0" x2="0" y2="1">
        <stop offset="0" stop-color="var(--pond-green)"/>
        <stop offset="0.35" stop-color="#7f9c58"/>
        <stop offset="0.55" stop-color="var(--pond-blue)"/>
        <stop offset="1" stop-color="#3d5e7c"/>
      </linearGradient>
    </defs>

    <rect class="sky-backdrop" x="0" y="0" width="600" height="400" fill="url(#skyFill)" role="img" aria-label="Cloudy sky over open country"/>

    <rect class="forest-photo" x="280" y="70" width="320" height="180" fill="url(#forestFill)" role="img" aria-label="Tall pine timber stand with grassy floor"/>

    <rect class="faded-trees-photo" x="330" y="250" width="270" height="150" fill="var(--faded-tree)" role="img" aria-label="Faded view of green treeline"/>

    <polygon class="pond-photo" points="0,218 330,218 330,395 0,395" fill="url(#pondFill)" stroke="#1f1f1f" stroke-width="4" role="img" aria-label="Still pond reflecting trees"/>

    <polygon class="farm-photo" points="0,70 250,70 345,152 270,212 0,212" fill="url(#fieldFill)" stroke="#1f1f1f" stroke-width="5" role="img" aria-label="Rows of green crops with a tractor spraying"/>

    <rect x="0" y="396" width="600" height="4" fill="#1f1f1f"/>

    <!-- Brand -->
    <rect x="392" y="24" width="14" height="14" fill="#1f1f1f"/>
    <text class="brand-name" x="412" y="31" font-size="11.5" fill="#1f1f1f">Sol Brantham</text>
    <text class="brand-name" x="412" y="46" font-size="11.5" fill="#1f1f1f">Summit Realty</text>

    <!-- Headline bands -->
    <rect x="40" y="246" width="292" height="32" fill="var(--accent-yellow)"/>
    <text class="headline" x="52" y="270" font-size="19" fill="#1f1f1f">HAVE A LAND FOR SALE?</text>
    <rect x="60" y="280" width="272" height="26" fill="#1f1f1f"/>
    <text class="subhead" x="70" y="298" font-size="13" fill="#ffffff">We Specialize in Rural Land Sales</text>

    <!-- Disclosure -->
    <rect x="340" y="262" width="260" height="18" fill="#1f1f1f"/>
    <text class="disclosure" x="350" y="275" font-size="8.6" fill="#ffffff">Not intended to solicit currently listed properties.</text>

    <!-- Compliance badges -->
    <rect x="488" y="300" width="32" height="28" fill="#1f1f1f"/>
    <text class="badge-caption" x="504" y="338" font-size="5" fill="#1f1f1f" text-anchor="middle">FAIR DWELLING ACCESS</text>
    <rect x="544" y="298" width="30" height="30" fill="#1f1f1f"/>
    <text class="badge-caption" x="559" y="338" font-size="5" fill="#1f1f1f" text-anchor="middle">HOMEVEST</text>
  </svg>
</section>

</body>
</html>
```